Redesign of page from emergency manual

Please redesign this PDF to look better. Please don't include any stock photos. It must be legible. Making some words bold is probably a good idea.

Here are some things I like :

https://tarrowbooks.com.au/collections/frontpage/products/the-plk-v2-ebook

https://img-cd.vostramediafiles.com/qa-ejkwPLOTYY_SuCKbZNu411Qwgjv8YssPxEdzXN93hDkSRjLXK8WmfgbmrJW4ZZ3yUPK=w1052-h592-rw

```html
<!DOCTYPE html>
<html lang="en">
<head>
<meta charset="utf-8">
<title>Hypertension, Acute</title>
<link rel="stylesheet" href="https://fonts.googleapis.com/css2?family=Open+Sans:wght@400;600;700;800&display=swap">
<style>
  :root {
    --brand-blue: #0b6dad;
    --navy: #133b74;
    --purple: #5a63ad;
    --sky: #2ea8de;
    --teal: #52c3ab;
    --green: #6cc06c;
    --caution: #8cc04e;
    --yellow: #f4d03f;
    --white: #ffffff;
    --ink: #1a1a1a;
  }
  * { box-sizing: border-box; margin: 0; padding: 0; }
  html, body { width: 1200px; height: 1000px; overflow: hidden; background: var(--white); }
  body { font-family: "Open Sans", sans-serif; color: var(--ink); }
  .page { position: relative; width: 1200px; height: 1000px; }
  .header-shape { position: absolute; left: 0; top: 0; width: 1200px; height: 113px; }
  .title {
    position: absolute; left: 136px; top: 46px; color: var(--white);
    font-size: 44px; font-weight: 700; letter-spacing: 0.5px; line-height: 54px;
  }
  .definition {
    position: absolute; left: 735px; top: 51px; width: 330px; height: 45px;
    background: var(--white); border-radius: 24px; color: var(--brand-blue);
    font-size: 10px; font-weight: 700; letter-spacing: 1.6px; line-height: 12px;
    text-align: center; display: flex; align-items: center; justify-content: center;
  }
  .intro {
    position: absolute; left: 36px; top: 130px; width: 700px;
    color: var(--brand-blue); font-size: 22px; font-weight: 800; line-height: 25px;
  }
  .checks { position: absolute; left: 36px; top: 218px; width: 680px; list-style: none; font-size: 19px; line-height: 22px; }
  .checks li { position: relative; padding-left: 24px; margin-bottom: 12px; }
  .checks li::before { content: ""; position: absolute; left: 0; top: 5px; width: 12px; height: 12px; background: var(--brand-blue); }
  .checks .sub { display: block; margin-top: 6px; }
  .bp-range {
    position: absolute; left: 747px; top: 134px; width: 398px; height: 201px;
    background: var(--brand-blue); border-radius: 18px; padding: 8px 5px;
  }
  .bp-title { text-align: center; font-size: 11px; font-weight: 700; letter-spacing: 2.6px; line-height: 13px; color: var(--white); }
  .bp-title .accent { color: var(--yellow); }
  .bp-grid { display: grid; grid-template-columns: repeat(3, 115px); column-gap: 21px; row-gap: 16px; margin-top: 6px; }
  .bp-cell {
    background: var(--white); border-radius: 7px; height: 24px; line-height: 24px;
    text-align: center; font-size: 12px; font-weight: 700; color: var(--ink);
  }
  .bp-cell.head { color: var(--navy); font-size: 11px; margin-bottom: 6px; }
  .caution {
    position: absolute; left: 40px; top: 347px; width: 1106px; height: 68px;
    background: var(--caution); border-radius: 18px; color: var(--white);
    font-size: 16.5px; line-height: 19px; padding: 5px 20px;
  }
  .caution strong { font-weight: 800; }
  .drug-table { position: absolute; left: 71px; top: 433px; width: 1058px; }
  .table-head {
    position: absolute; left: 0; top: 0; width: 1058px; height: 38px; background: var(--brand-blue);
    color: var(--white); font-size: 21px; font-weight: 700; letter-spacing: 4.5px; line-height: 38px;
  }
  .table-head .col-action { position: absolute; left: 90px; }
  .table-head .col-drug { position: absolute; left: 540px; }
  .row { position: absolute; left: 0; width: 1058px; color: var(--white); }
  .row.vaso { top: 57px; height: 66px; background: var(--purple); }
  .row.beta { top: 139px; height: 96px; background: var(--sky); }
  .row.ccb { top: 252px; height: 63px; background: var(--teal); }
  .row.dopa { top: 332px; height: 38px; background: var(--green); }
  .action {
    position: absolute; left: 17px; top: 50%; transform: translateY(-50%);
    font-size: 15px; font-weight: 700; letter-spacing: 3.2px; line-height: 17px;
  }
  .doses { position: absolute; left: 405px; top: 50%; transform: translateY(-50%); list-style: none; }
  .doses li {
    position: relative; padding-left: 28px; font-size: 11.5px; font-weight: 700;
    letter-spacing: 2.4px; line-height: 13px; margin: 11px 0;
  }
  .doses li::before { content: ""; position: absolute; left: 0; top: 1px; width: 12px; height: 12px; background: var(--white); }
  .differential-title {
    position: absolute; left: 44px; top: 830px; color: var(--navy);
    font-size: 27px; font-weight: 700; line-height: 34px; padding-left: 40px;
  }
  .differential-title::before { content: ""; position: absolute; left: 0; top: 9px; width: 17px; height: 17px; background: var(--navy); }
  .dx { position: absolute; list-style: none; color: var(--brand-blue); font-size: 17px; line-height: 19px; }
  .dx li { position: relative; padding-left: 26px; margin-bottom: 15px; }
  .dx li::before { content: ""; position: absolute; left: 0; top: 5px; width: 10px; height: 10px; border-radius: 50%; background: var(--brand-blue); }
  .dx.col-1 { left: 102px; top: 872px; width: 300px; }
  .dx.col-2 { left: 483px; top: 872px; width: 330px; }
  .dx.col-3 { left: 909px; top: 872px; width: 240px; }
  .dx.col-3 li { margin-bottom: 11px; }
  .side-tab {
    position: absolute; left: 1163px; top: 368px; width: 29px; height: 476px;
    background: var(--brand-blue); border-radius: 15px;
    display: flex; align-items: center; justify-content: center;
  }
  .side-tab span {
    writing-mode: vertical-rl; color: var(--white); font-size: 21px; font-weight: 800; letter-spacing: 9px;
  }
  .dot { position: absolute; border-radius: 50%; }
  .dot.sky { width: 22px; height: 22px; background: var(--sky); left: 1167px; }
  .dot.purple { width: 32px; height: 32px; background: var(--purple); left: 1162px; }
</style>
</head>
<body>
<main class="page">
  <svg class="header-shape" viewBox="0 0 1200 113" preserveAspectRatio="none" aria-hidden="true">
    <rect x="0" y="0" width="1200" height="113" fill="#0b6dad"/>
    <polygon points="0,113 69,13 69,73 118,63 118,113" fill="#ffffff"/>
    <polygon points="1200,113 1131,13 1131,73 1082,63 1082,113" fill="#ffffff"/>
  </svg>
  <h1 class="title">HYPERTENSION, ACUTE</h1>
  <div class="definition">SUSTAINED HIGH BLOOD PRESSURE<br>REFRACTORY TO TREATING<br>REVERSIBLE CAUSES</div>

  <p class="intro">In pediatrics, hypertension is almost always treated by addressing likely causes such as light anesthesia or measurement error:</p>
  <ul class="checks">
    <li>Ensure correct BP cuff size: cuff bladder<br>width ~ 40% of limb circumference</li>
    <li>Ensure arterial line transducer is at level of heart
      <span class="sub">- Consider placing arterial line if not already present</span></li>
  </ul>

  <section class="bp-range">
    <h2 class="bp-title"><span class="accent">HYPERTENSIVE</span><br>BLOOD PRESSURE RANGE*</h2>
    <div class="bp-grid">
      <div class="bp-cell head">AGE (YR)</div><div class="bp-cell head">SYSTOLIC</div><div class="bp-cell head">DIASTOLIC</div>
      <div class="bp-cell">NEWBORN</div><div class="bp-cell">&gt;97</div><div class="bp-cell">&gt;70</div>
      <div class="bp-cell">1-3</div><div class="bp-cell">&gt;105</div><div class="bp-cell">&gt;61</div>
      <div class="bp-cell">4-12</div><div class="bp-cell">&gt;113</div><div class="bp-cell">&gt;86</div>
    </div>
  </section>

  <p class="caution"><strong>CAUTION:</strong> Anti-hypertensive drugs are almost never needed for routine pediatric cases. These medications are used almost exclusively for specialized cardiac, neurosurgical, or endocrine (pheochromocytoma) cases. Consult an expert before use. Rule-out increased ICP.</p>

  <section class="drug-table">
    <div class="table-head"><span class="col-action">ACTION</span><span class="col-drug">DRUG (IV DOSING)</span></div>
    <div class="row vaso">
      <div class="action">DIRECT SMOOTH MUSCLE<br>RELAXATION</div>
      <ul class="doses">
        <li>SODIUM NITROPRUSSIDE 0.5-10 MICROGRAMS/KG/MIN</li>
        <li>HYDRALAZINE 0.1-0.2 MG/KG (ADULT DOSE 5-10 MG)</li>
      </ul>
    </div>
    <div class="row beta">
      <div class="action">B-ADRENERGIC<br>BLOCKADE</div>
      <ul class="doses">
        <li>ESMOLOL 100-500 MICROGRAMS/KG OVER 5 MIN, THEN<br>25-300 MICROGRAMS/KG/MIN</li>
        <li>LABETALOL (ALSO A EFFECT) 0.2-1 MG/KG Q 10 MIN;<br>0.4-3 MG/KG/HOUR (INFUSION)</li>
      </ul>
    </div>
    <div class="row ccb">
      <div class="action">CALCIUM CHANNEL<br>BLOCKADE</div>
      <ul class="doses">
        <li>NICARDAPINE 0.5-5 MICROGRAMS/KG/MIN</li>
        <li>CLEVIDIPINE 0.5-3.5 MICROGRAMS/KG/MIN</li>
      </ul>
    </div>
    <div class="row dopa">
      <div class="action">D1-DOPAMINE AGONIST</div>
      <ul class="doses">
        <li>FENOLDOPAM 0.2-0.8 MICROGRAMS/KG/MIN</li>
      </ul>
    </div>
  </section>

  <h2 class="differential-title">CONSIDER DIFFERENTIAL (PARTIAL):</h2>
  <ul class="dx col-1">
    <li>Light anesthesia (consider vaporizer or infusion pump empty or malfunctioning)</li>
    <li>Hypercarbia</li>
  </ul>
  <ul class="dx col-2">
    <li>Hypoxemia</li>
    <li>Arterial line transducer too<br>low or BP cuff too small</li>
    <li>Withdrawal (EtOH or opioid)</li>
  </ul>
  <ul class="dx col-3">
    <li>Thyroid Storm</li>
    <li>Pheochromocytoma</li>
    <li>Drug Error</li>
  </ul>

  <div class="dot sky" style="top:290px"></div>
  <div class="dot purple" style="top:324px"></div>
  <div class="side-tab"><span>HYPERTENSION, ACUTE</span></div>
  <div class="dot purple" style="top:860px"></div>
  <div class="dot sky" style="top:905px"></div>
</main>
</body>
</html>
```